Website for PeakStride Functional Training

We would like to launch a website for our boutique gym, PeakStride Functional Training. We'd like the website to have a lot of lime green which is one of our colors in our logo. The website will have a description of our workouts, membership, free trial class and location information.

Target Market(s)

Fitness enthusiasts, health conscious people, target ages 20-65, people looking to get fit and healthy, people looking to lose weight

Industry/Entity Type

Gym

Coding

Number of Pages Required

1 page

Font styles to use
Serif

Colors
9ccb3b
34a7d8

Requirements
Must have
• A lot of lime green to match our logo. Let the website be fun, eye catchy. Our phone number which is 614-287-9153 to be easily dialed directly from our website.
Nice to have
• We would like to include this verbiage:
• -The Most FUN 1 hour workout
• -Affordable personal training/group training
• -Individualized workout programs
• -FUN workouts delivering results
• -Turn ON fat burn-The Most FUN 1 hour workout
• -Turn ON fat burning "EPOC" after burn
• We want our website to be easily seen on smart phones, iPads, Androids
Should not have
• Font that is hard on the eyes

```html
<!DOCTYPE html>
<html lang="en">
<head>
<meta charset="utf-8">
<title>PeakStride Functional Training</title>
<meta name="viewport" content="width=1200">
<link href="https://fonts.googleapis.com/css2?family=Play:wght@400;700&family=Montserrat:wght@400;500&family=Open+Sans:wght@400;600&display=swap" rel="stylesheet">
<style>
:root{
  --lime:#9ac93a;
  --lime-dark:#86b52c;
  --teal:#55c5c6;
  --ink:#111;
  --white:#fff;
  --header-bg:#f4f4f4;
  --footer-dark:#444;
  --hero-a:#5f7d1c;
  --hero-b:#1d2a08;
  --grey-text:#666;
}
*{box-sizing:border-box;margin:0;padding:0}
html,body{width:1200px;height:2270px;overflow:hidden}
body{position:relative;font-family:"Play",sans-serif;color:var(--ink);background:var(--white)}
a{color:inherit;text-decoration:none}

.site-header{position:absolute;left:0;top:0;width:1200px;height:71px;background:var(--header-bg);border-top:5px solid var(--lime)}
.brand{position:absolute;left:136px;top:10px;line-height:1}
.brand-name{display:block;font-family:"Play",sans-serif;font-weight:700;font-size:30px;color:var(--lime);letter-spacing:1px}
.brand-tag{display:block;font-family:"Play",sans-serif;font-weight:700;font-size:15px;color:var(--lime);margin-top:3px}
.header-call{position:absolute;left:920px;top:31px;font-family:"Open Sans",sans-serif;font-weight:600;font-size:12px;color:var(--grey-text);white-space:nowrap}

.main-nav{position:absolute;left:0;top:71px;width:1200px;height:36px;background:var(--white)}
.main-nav a{position:absolute;top:0;height:36px;line-height:36px;font-family:"Montserrat",sans-serif;font-size:12px;color:var(--ink);white-space:nowrap}
.main-nav a.active{background:var(--lime);color:var(--white);left:136px;width:67px;text-align:center}
.social-dot{position:absolute;top:84px;width:10px;height:10px;border-radius:50%;background:var(--ink)}

.hero{position:absolute;left:0;top:107px;width:1200px;height:554px;background:radial-gradient(ellipse at 60% 40%,var(--hero-a),var(--hero-b) 75%)}
.hero-photo{position:absolute;left:141px;top:62px;width:376px;height:433px;background:linear-gradient(135deg,#8a8c8f,#c9c3bf 50%,#5b5d61)}
.hero-title{position:absolute;left:569px;top:80px;color:var(--white);font-weight:700;line-height:1;white-space:nowrap}
.hero-title .small{display:block;font-size:42px}
.hero-title .big{display:block;font-size:54px;margin-top:16px}
.hero-points{position:absolute;left:573px;top:206px;list-style:none;color:var(--white);font-weight:700;font-size:16px;white-space:nowrap}
.hero-points li{height:40px;display:flex;align-items:center;gap:10px}
.cta{position:absolute;left:572px;top:418px;height:43px;display:flex;white-space:nowrap}
.cta-label{background:var(--lime);color:var(--white);font-weight:700;font-size:20px;line-height:43px;width:154px;text-align:center;white-space:nowrap}
.cta-arrow{width:40px;background:var(--teal);display:flex;align-items:center;justify-content:center}

.welcome{position:absolute;left:0;top:661px;width:1200px;height:260px;background:var(--teal);color:var(--white);text-align:center}
.section-title{font-weight:700;font-size:42px;line-height:1}
.welcome .section-title{margin-top:58px}
.band-text{width:820px;margin:20px auto 0;font-weight:700;font-size:16px;line-height:24px}

.feature{position:absolute;left:0;width:1200px}
.classes{top:921px;height:397px;border-bottom:1px solid #ccc}
.professionals{top:1318px;height:384px}
.feature-photo{position:absolute}
.classes .feature-photo{left:136px;top:61px;width:407px;height:285px;border:2px solid var(--lime);background:linear-gradient(135deg,#e9d9c2,#c9a57c 55%,#9aa4a8)}
.professionals .feature-photo{left:655px;top:51px;width:409px;height:285px;background:linear-gradient(135deg,#b7c7d3,#d98a5a 45%,#6f7f8e)}
.feature-title{position:absolute;font-weight:700;font-size:33px;color:var(--lime);line-height:1;white-space:nowrap}
.feature-text{position:absolute;width:468px;font-weight:700;font-size:16px;line-height:28px}
.btn{position:absolute;height:44px;line-height:44px;width:141px;text-align:center;background:var(--lime);font-weight:700;font-size:19px;color:var(--ink);white-space:nowrap}

.testimonial{position:absolute;left:0;top:1702px;width:1200px;height:439px;background:var(--lime);color:var(--white);text-align:center}
.testimonial .section-title{margin-top:40px}
.testimonial .band-text{margin-top:26px}
.avatar{position:absolute;left:528px;top:201px;width:142px;height:142px;border-radius:50%;background:linear-gradient(180deg,#e6e6e6,#b9b9b9)}
.reviewer{position:absolute;left:0;width:1200px;top:365px;font-family:"Open Sans",sans-serif;font-weight:600;font-size:14px}
.reviewer-role{position:absolute;left:0;width:1200px;top:388px;font-weight:700;font-size:16px}

.contact-bar{position:absolute;left:0;top:2141px;width:1200px;height:88px;background:var(--teal);color:var(--white)}
.contact-item{position:absolute;top:0;height:88px}
.contact-item svg{position:absolute;top:20px}
.contact-head{position:absolute;top:20px;font-weight:700;font-size:19px;white-space:nowrap}
.contact-body{position:absolute;top:44px;font-family:"Open Sans",sans-serif;font-size:12px;line-height:15px;white-space:nowrap}
.contact-body.large{font-size:17px;top:46px}
.legal{position:absolute;left:0;top:2229px;width:1200px;height:41px;background:var(--footer-dark);color:#ddd;text-align:center;line-height:41px;font-family:"Open Sans",sans-serif;font-size:11px}
</style>
</head>
<body>

<header class="site-header">
  <a class="brand" href="#">
    <span class="brand-name">PEAKSTRIDE</span>
    <span class="brand-tag">Functional Training</span>
  </a>
  <a class="header-call" href="tel:6142879153">Call Us:&nbsp; 614-287-9153</a>
</header>

<nav class="main-nav">
  <a class="active" href="#">HOME</a>
  <a href="#" style="left:230px">ABOUT US</a>
  <a href="#" style="left:333px">MEMBERSHIP</a>
  <a href="#" style="left:454px">TRAINERS</a>
  <a href="#" style="left:554px">BLOG</a>
  <a href="#" style="left:629px">GALLERY</a>
  <a href="#" style="left:725px">CONTACT US</a>
</nav>
<span class="social-dot" style="left:1009px"></span>
<span class="social-dot" style="left:1040px"></span>

<section class="hero">
  <div class="hero-photo" role="img" aria-label="Trainer guiding a smiling member on a gym machine"></div>
  <h1 class="hero-title"><span class="small">THE MOST FUN</span><span class="big">1 HOUR WORKOUT</span></h1>
  <ul class="hero-points">
    <li><svg width="16" height="14" viewBox="0 0 16 14"><path d="M1 7l5 5L15 2" fill="none" stroke="#fff" stroke-width="3"/></svg>Affordable personal training/group training</li>
    <li><svg width="16" height="14" viewBox="0 0 16 14"><path d="M1 7l5 5L15 2" fill="none" stroke="#fff" stroke-width="3"/></svg>Individualized workout programs</li>
    <li><svg width="16" height="14" viewBox="0 0 16 14"><path d="M1 7l5 5L15 2" fill="none" stroke="#fff" stroke-width="3"/></svg>FUN workouts delivering results</li>
    <li><svg width="16" height="14" viewBox="0 0 16 14"><path d="M1 7l5 5L15 2" fill="none" stroke="#fff" stroke-width="3"/></svg>Turn ON fat burn-The Most FUN 1 hour workout</li>
    <li><svg width="16" height="14" viewBox="0 0 16 14"><path d="M1 7l5 5L15 2" fill="none" stroke="#fff" stroke-width="3"/></svg>Turn ON fat burning “EPOC” after burn</li>
  </ul>
  <a class="cta" href="#">
    <span class="cta-label">START TODAY</span>
    <span class="cta-arrow"><svg width="16" height="24" viewBox="0 0 16 24"><path d="M3 3l9 9-9 9" fill="none" stroke="#fff" stroke-width="4"/></svg></span>
  </a>
</section>

<section class="welcome">
  <h2 class="section-title">WELCOME</h2>
  <p class="band-text">Lorem ipsum dolor sit amet, consectetuer adipiscing elit, sed diam nonummy nibh euismod tincidunt ut<br>laoreet dolore magna aliquam erat volutpat. Ut wisi enim ad minim veniam, quis nostrud exerci tation ulla-<br>mcorper suscipit lobortis nisl</p>
</section>

<section class="feature classes">
  <div class="feature-photo" role="img" aria-label="Group step class with exercise balls in the background"></div>
  <h2 class="feature-title" style="left:572px;top:56px">OUR CLASSES</h2>
  <p class="feature-text" style="left:575px;top:112px">Lorem ipsum dolor sit amet, consectetuer adipiscing elit, sed diam nonummy nibh euismod tincidunt ut laoreet dolore magna aliquam erat volutpat. Ut wisi enim ad minim veniam, quis nostrud exerci tation ullamcorper suscipit.</p>
  <a class="btn" href="#" style="left:575px;top:252px">READ MORE</a>
</section>

<section class="feature professionals">
  <h2 class="feature-title" style="left:136px;top:46px">FITNESS PROFESSIONALS</h2>
  <p class="feature-text" style="left:136px;top:105px">Lorem ipsum dolor sit amet, consectetuer adipiscing elit, sed diam nonummy nibh euismod tincidunt ut laoreet dolore magna aliquam erat volutpat. Ut wisi enim ad minim veniam, quis nostrud exerci tation ullamcorper suscipit.</p>
  <a class="btn" href="#" style="left:136px;top:245px">READ MORE</a>
  <div class="feature-photo" role="img" aria-label="Trainer and member giving a high five in the gym"></div>
</section>

<section class="testimonial">
  <h2 class="section-title">TESTIMONIAL</h2>
  <p class="band-text">Lorem ipsum dolor sit amet, consectetuer adipiscing elit, sed diam nonummy nibh euismod tincidunt ut<br>laoreet dolore magna aliquam erat volutpat. Ut wisi enim ad minim<br>quis nostrud exerci tation ullamcorper suscipit lobortis nisl</p>
  <div class="avatar" role="img" aria-label="Portrait of the reviewing member"></div>
  <p class="reviewer">DEAN HARLOW</p>
  <p class="reviewer-role">LOREM IPSUM DOLOR SIT</p>
</section>

<footer class="contact-bar">
  <div class="contact-item" style="left:196px">
    <svg width="34" height="40" viewBox="0 0 34 40"><path d="M17 3c-6 0-10 4.5-10 10 0 7 10 17 10 17s10-10 10-17c0-5.5-4-10-10-10z" fill="none" stroke="#fff" stroke-width="3"/><circle cx="17" cy="13" r="3.5" fill="#fff"/><ellipse cx="17" cy="35" rx="12" ry="3" fill="none" stroke="#fff" stroke-width="2"/></svg>
    <span class="contact-head" style="left:66px">Visit Us</span>
    <span class="contact-body" style="left:64px">Lorem ipsum dolor sit amet<br>consetetur sadipscing</span>
  </div>
  <a class="contact-item" href="tel:6142879153" style="left:532px">
    <svg width="38" height="44" viewBox="0 0 38 44"><rect x="3" y="8" width="20" height="32" rx="2" fill="none" stroke="#fff" stroke-width="3"/><line x1="8" y1="16" x2="18" y2="16" stroke="#fff" stroke-width="2"/><line x1="8" y1="22" x2="18" y2="22" stroke="#fff" stroke-width="2"/><line x1="8" y1="28" x2="18" y2="28" stroke="#fff" stroke-width="2"/><path d="M20 12c4-6 10-8 14-6l-4-4m4 4l-5 2" fill="none" stroke="#fff" stroke-width="3"/></svg>
    <span class="contact-head" style="left:66px">Call Us</span>
    <span class="contact-body large" style="left:66px">614-287-9153</span>
  </a>
  <div class="contact-item" style="left:822px">
    <svg width="48" height="42" viewBox="0 0 48 42"><path d="M3 16L24 3l21 13v23H3z" fill="none" stroke="#fff" stroke-width="3"/><path d="M3 16l21 14 21-14" fill="none" stroke="#fff" stroke-width="3"/><circle cx="24" cy="15" r="4" fill="none" stroke="#fff" stroke-width="2"/></svg>
    <span class="contact-head" style="left:87px;top:18px">Email</span>
    <span class="contact-body" style="left:86px;top:48px">info@peakstridefit.com</span>
  </div>
</footer>
<div class="legal">Copyright © 2017. All rights reserved.</div>

</body>
</html>
```